TRENDY & MODERN BUSINESS CARD DESIGN for Media Company *

I need a minimalistic - clean - modern and professional business card layout and design for MEDIA & PHOTOGRAPHY STUDIO.

We do NOT have a logo, and not really looking for one - but rather excellent typography and design. We would consider the 3 as a focal point.

We do personal and commercial photography.

Target Market(s)

Personal and commercial photography clientele

Contact Information for Business Card

ZUB size - from zub.com / size guidelines are enclosed in the brief

Font styles to use
Sans Serif

Colors
f78f20
eda3c7
cee9f5
0555a3
e667a6
fbf289

Requirements
Must have
• Clean lines - Modern layout
Nice to have
• All blue background as an option - use color palette in brief please.
Should not have
• Old fashion fonts and regular fonts.

```html
<!DOCTYPE html>
<html lang="en">
<head>
<meta charset="utf-8">
<title>Lumen Ninth – Business Card</title>
<link rel="stylesheet" href="https://fonts.googleapis.com/css2?family=Source+Sans+3:wght@400;600&display=swap">
<style>
  :root {
    --brand-blue: #0c4c89;
    --link-blue: #1f4f92;
    --ink: #2b2b2b;
    --paper: #fdfdfd;
    --backdrop: #eeeeee;
  }
  * { margin: 0; padding: 0; box-sizing: border-box; }
  html, body { width: 1200px; height: 1200px; overflow: hidden; }
  body {
    background: var(--backdrop);
    font-family: "Source Sans 3", sans-serif;
    color: var(--ink);
    position: relative;
  }
  .card {
    position: absolute;
    left: 184px;
    width: 831px;
    height: 557px;
    background: var(--paper);
    overflow: hidden;
  }
  .card--front { top: 19px; }
  .card--back { top: 631px; }

  .front-band {
    position: absolute;
    left: 0; top: 0;
    width: 100%; height: 351px;
    background: var(--brand-blue);
  }
  .front-brand {
    position: absolute;
    left: 80px; top: 132px;
    color: #ffffff;
  }
  .brand-name {
    display: block;
    font-weight: 400;
    font-size: 40px;
    line-height: 1;
    letter-spacing: 0.5px;
  }
  .brand-tagline {
    display: block;
    font-size: 12px;
    margin-top: 6px;
    letter-spacing: 0.2px;
  }
  .holder {
    position: absolute;
    left: 82px; top: 386px;
  }
  .holder-name {
    font-size: 30px;
    font-weight: 400;
    line-height: 1;
    color: #333;
  }
  .holder-title {
    font-size: 15px;
    margin-top: 14px;
    color: #333;
  }

  .contact-panel {
    position: absolute;
    left: 470px; top: 253px;
    width: 295px; height: 304px;
    background: var(--paper);
  }
  .contact-row {
    position: absolute;
    left: 0;
    width: 100%;
    font-size: 14.5px;
    line-height: 21px;
    color: #222;
  }
  .contact-row svg {
    position: absolute;
    left: 28px; top: 1px;
    width: 20px; height: 20px;
    fill: var(--brand-blue);
  }
  .contact-row p { margin-left: 84px; }
  .row-phone { top: 22px; }
  .row-mail { top: 56px; }
  .row-address { top: 91px; }
  .row-web { top: 137px; }
  .row-cities { top: 172px; }

  .back-brand {
    position: absolute;
    left: 0; top: 205px;
    width: 100%;
    text-align: center;
    color: var(--brand-blue);
  }
  .back-brand .brand-name { font-size: 70px; letter-spacing: 1px; }
  .back-brand .brand-tagline { font-size: 20px; margin-top: 12px; color: #1a3f70; }
  .back-url {
    position: absolute;
    left: 0; top: 376px;
    width: 100%;
    text-align: center;
    font-size: 27px;
    font-weight: 600;
    color: var(--link-blue);
  }
</style>
</head>
<body>

<section class="card card--front" aria-label="Card front">
  <div class="front-band"></div>
  <div class="front-brand">
    <span class="brand-name">Lumen Ninth</span>
    <span class="brand-tagline">Framing Moments. Telling Stories.</span>
  </div>
  <div class="holder">
    <h1 class="holder-name">Marisol Vantera</h1>
    <p class="holder-title">Founder &amp; Media Director</p>
  </div>

  <div class="contact-panel">
    <div class="contact-row row-phone">
      <svg viewBox="0 0 24 24" aria-hidden="true"><path d="M6.6 10.8a15 15 0 0 0 6.6 6.6l2.2-2.2c.3-.3.7-.4 1-.2 1.1.4 2.3.6 3.6.6.6 0 1 .4 1 1V20c0 .6-.4 1-1 1A17 17 0 0 1 3 4c0-.6.4-1 1-1h3.5c.6 0 1 .4 1 1 0 1.3.2 2.5.6 3.6.1.3 0 .7-.2 1z"/></svg>
      <p>(555) 014-2287</p>
    </div>
    <div class="contact-row row-mail">
      <svg viewBox="0 0 24 24" aria-hidden="true"><path d="M3 10l9-6 9 6v10H3z"/></svg>
      <p>mv@lumenninthmedia.com</p>
    </div>
    <div class="contact-row row-address">
      <svg viewBox="0 0 24 24" aria-hidden="true"><path d="M12 3l10 9h-3v9h-5v-6h-4v6H5v-9H2z"/></svg>
      <p>2400 Harbor Av 9th Floor<br>Coral Bay, FL 33100</p>
    </div>
    <div class="contact-row row-web">
      <svg viewBox="0 0 24 24" aria-hidden="true"><path d="M12 2a10 10 0 1 0 0 20 10 10 0 0 0 0-20zm-1 2.1V8H7.4A8 8 0 0 1 11 4.1zm2 0A8 8 0 0 1 16.6 8H13zM5.3 10H11v4H5.3a8 8 0 0 1 0-4zm7.7 0h5.7a8 8 0 0 1 0 4H13zm-5.6 6H11v3.9A8 8 0 0 1 7.4 16zm5.6 0h3.6a8 8 0 0 1-3.6 3.9z"/></svg>
      <p>mv@lumenninthmedia.com</p>
    </div>
    <div class="contact-row row-cities">
      <svg viewBox="0 0 24 24" aria-hidden="true"><path d="M12 2a7 7 0 0 0-7 7c0 5 7 13 7 13s7-8 7-13a7 7 0 0 0-7-7zm0 4.5a2.5 2.5 0 1 1 0 5 2.5 2.5 0 0 1 0-5z"/></svg>
      <p>Tampa • Boston •<br>Denver • Tulum • Milano</p>
    </div>
  </div>
</section>

<section class="card card--back" aria-label="Card back">
  <div class="back-brand">
    <span class="brand-name">Lumen Ninth</span>
    <span class="brand-tagline">Framing Moments. Telling Stories.</span>
  </div>
  <p class="back-url">www.lumenninthmedia.com</p>
</section>

</body>
</html>
```